Massage Therapy and Energy Healing Practice

I am a massage therapist, Reiki energy healer, I sell herbs and oils, and also a health lifestyle coach. I need a design that is strong because I'm not a spa. I do therapeutic work, but I want a touch of the energy and spiritual healing I do as well to be included in the design. I like blue, green, or purple colors. I live in the Blue Ridge Mountains of VA and even though my practice is in the city I like my love for nature and the earth to show through. I would like a single image logo so I can use the image many places. I need a strong brand that will let others know that I combine massage therapy in a therapeutic way while keeping my touches of energy healing, nurturing, herb crafting, and mother earth loving ways.
Updates

Just some things about me:I like to hike. I live on a farm. I own horses, cows, sheep and dogs. I love nature and the energy in produces. I'm very spiritual. I don't know how these things might help or if they do, but I know that my personality might help inspire what I will find good in a design. Added Sunday, December 13, 2015

Target Market(s)

People in pain. People who need spiritual council. Need herbal medicine advice. Holistic healthcare.

Industry/Entity Type

Massage

Contact Information for Business Card

Kneadwell Studio
Lorna T. Whitcombe C.M.T, R.M.T
40519 Hollin Creek Court, Tallowdale, VA
540-718-2437

Colors
3176b5
85abd2
876aae
9bcb3c

Requirements
Must have
• Strong Branding that promotes my massage therapy practice first
Nice to have
• Something to evoke my herbal medicine, my energy healing, my spiritual side

```html
<!DOCTYPE html>
<html lang="en">
<head>
<meta charset="utf-8">
<title>Kneadwell Studio — Business Card</title>
<link rel="stylesheet" href="https://fonts.googleapis.com/css2?family=Source+Sans+3:wght@400;600&display=swap">
<style>
  :root {
    --backdrop: #e9e6e1;
    --card: #ffffff;
    --ink: #1f1f1f;
    --ink-soft: #333333;
    --band-blue: #2f6db3;
    --photo-sky: #4f6f6a;
    --photo-barn: #7f8a86;
    --photo-herd: #9c6a48;
    --photo-grass: #3f9a2e;
  }
  html, body {
    margin: 0;
    width: 1200px;
    height: 902px;
    overflow: hidden;
    background: var(--backdrop);
  }
  .canvas {
    position: relative;
    width: 1200px;
    height: 902px;
    display: flex;
    align-items: center;
    justify-content: center;
  }
  .business-card {
    position: relative;
    width: 900px;
    height: 640px;
    background: var(--card);
    box-shadow: 0 10px 30px rgba(0,0,0,0.18);
    overflow: hidden;
    font-family: "Source Sans 3", "Myriad Pro", sans-serif;
    color: var(--ink);
  }
  .photo-panel {
    position: absolute;
    inset: 0;
    width: 900px;
    height: 640px;
  }
  .card-text {
    position: absolute;
    right: 48px;
    text-align: right;
  }
  .brand-name {
    top: 40px;
    font-size: 66px;
    font-weight: 400;
    letter-spacing: 0.5px;
    margin: 0;
  }
  .practitioner {
    top: 250px;
  }
  .practitioner-name {
    font-size: 44px;
    font-weight: 400;
    margin: 0;
    line-height: 1.05;
  }
  .credentials {
    font-size: 22px;
    color: var(--ink-soft);
    margin: 2px 0 0;
  }
  .contact {
    bottom: 60px;
    font-size: 24px;
    line-height: 1.35;
  }
  .contact p { margin: 0; }
  .contact .phone { padding-right: 150px; }
</style>
</head>
<body>
<main class="canvas">
  <article class="business-card">
    <svg class="photo-panel" viewBox="0 0 900 640" aria-hidden="false">
      <defs>
        <linearGradient id="farm-scene" x1="0" y1="0" x2="0" y2="1">
          <stop offset="0" stop-color="var(--photo-sky)"/>
          <stop offset="0.35" stop-color="var(--photo-barn)"/>
          <stop offset="0.55" stop-color="var(--photo-herd)"/>
          <stop offset="0.8" stop-color="#b8a48c"/>
          <stop offset="1" stop-color="var(--photo-grass)"/>
        </linearGradient>
      </defs>
      <path role="img" aria-label="Photograph of horses, cows, sheep, pigs and ducks gathered on green grass in front of a barn"
            d="M0 0 H330 C380 180 420 420 450 640 H0 Z" fill="url(#farm-scene)"/>
      <path class="band-curve" d="M330 0 C380 180 420 420 450 640"
            fill="none" stroke="var(--band-blue)" stroke-width="12"/>
    </svg>

    <h1 class="card-text brand-name">Kneadwell Studio</h1>

    <div class="card-text practitioner">
      <p class="practitioner-name">Lorna T. Whitcombe</p>
      <p class="credentials">C.M.T, R.M.T</p>
    </div>

    <div class="card-text contact">
      <p class="phone">540-718-2437</p>
      <p class="address">40519 Hollin Creek Court, Tallowdale, VA</p>
    </div>
  </article>
</main>
</body>
</html>
```